Floor Inspections and Consulting

We provide inspections and consulting services on various floor coverings, e.g. carpet, hardwood, etc. We also do expert witness work for attorneys due to floor covering failures. We current have a logo, just need it incorporated into a new design. I have examples of cards I have found on the internet that capture my attention and make a statement. I have included our original business card, which in my opinion is terrible, but it does have our logo on it.

```html
<!DOCTYPE html>
<html lang="en">
<head>
<meta charset="utf-8">
<title>Keystone Floor Review – Business Cards</title>
<link rel="stylesheet" href="https://fonts.googleapis.com/css2?family=Montserrat:wght@400;500;600;700&display=swap">
<style>
  :root {
    --blue: #1f8bc0;
    --ink: #1c1c1c;
    --card-dark: #1f1f1f;
    --card-light: #f4f4f4;
    --stage: #e4e4e4;
    --white: #ffffff;
  }
  * { box-sizing: border-box; margin: 0; padding: 0; }
  html, body { width: 1200px; height: 1021px; overflow: hidden; }
  body {
    background: var(--stage);
    font-family: "Montserrat", sans-serif;
    position: relative;
  }
  .card {
    position: absolute;
    top: 90px;
    width: 480px;
    height: 840px;
    overflow: hidden;
    box-shadow: 0 10px 30px rgba(0,0,0,0.18);
  }
  /* ---------- front ---------- */
  .card-front { left: 80px; background: var(--card-light); }
  .card-front .edge-band {
    position: absolute; left: 0; top: 0; bottom: 0; width: 18px;
    background: var(--card-dark);
  }
  .brand {
    position: absolute; left: 0; right: 0;
    display: flex; flex-direction: column; align-items: center; gap: 18px;
  }
  .brand-mark {
    width: 120px; height: 120px; border-radius: 50%; background: var(--blue);
  }
  .brand-name {
    font-weight: 700; color: var(--blue); font-size: 30px;
    text-transform: uppercase; letter-spacing: 1px; text-align: center; line-height: 1.15;
  }
  .tagline {
    font-weight: 700; font-size: 17px; letter-spacing: 0.5px; text-align: center;
  }
  .card-front .brand { top: 70px; }
  .card-front .tagline { color: var(--ink); }
  .contact-list {
    position: absolute; left: 18px; right: 0; top: 440px; bottom: 0;
    list-style: none;
  }
  .contact-row {
    display: flex; align-items: center; height: 100px;
    border-top: 2px solid var(--ink);
  }
  .contact-row:first-child { border-top: none; }
  .contact-icon {
    width: 70px; height: 100%; background: var(--blue);
    display: flex; align-items: center; justify-content: center; flex: none;
  }
  .contact-icon svg { width: 28px; height: 28px; fill: var(--white); }
  .contact-text {
    padding-left: 30px; font-size: 21px; color: var(--ink); line-height: 1.3;
  }
  .person-name { color: var(--blue); font-weight: 700; font-size: 26px; text-transform: uppercase; }
  .person-role { text-transform: uppercase; font-size: 19px; }
  /* ---------- back ---------- */
  .card-back { left: 640px; background: var(--card-dark); }
  .accent-top {
    position: absolute; top: 0; left: 0; width: 46%; height: 20px; background: var(--blue);
  }
  .accent-bottom {
    position: absolute; bottom: 0; right: 0; width: 64%; height: 20px; background: var(--blue);
  }
  .card-back .brand { top: 230px; }
  .card-back .tagline { color: var(--white); }
  .service-line {
    position: absolute; left: 0; right: 0; bottom: 110px;
    color: var(--white); font-size: 20px; text-transform: uppercase;
    text-align: center; line-height: 1.35; letter-spacing: 0.5px;
  }
</style>
</head>
<body>
  <section class="card card-front" aria-label="Business card front">
    <div class="edge-band"></div>
    <div class="brand">
      <div class="brand-mark"></div>
      <div class="brand-name">Keystone<br>Floor Review</div>
      <div class="tagline">Analysis &amp; Consulting</div>
    </div>
    <ul class="contact-list">
      <li class="contact-row">
        <span class="contact-icon"><svg viewBox="0 0 24 24"><circle cx="8" cy="8" r="4"/><path d="M1 21c0-5 3-8 7-8s7 3 7 8z"/><path d="M15 9h8v12h-6c0-4-1-6-2-7z"/></svg></span>
        <div class="contact-text"><div class="person-name">Daniel Marrow</div><div class="person-role">Founder &amp; Owner</div></div>
      </li>
      <li class="contact-row">
        <span class="contact-icon"><svg viewBox="0 0 24 24"><path d="M6.6 10.8a15 15 0 0 0 6.6 6.6l2.2-2.2c.3-.3.7-.4 1-.2 1.1.4 2.3.6 3.6.6.6 0 1 .4 1 1V20c0 .6-.4 1-1 1A17 17 0 0 1 3 4c0-.6.4-1 1-1h3.5c.6 0 1 .4 1 1 0 1.3.2 2.5.6 3.6.1.3 0 .7-.2 1z"/></svg></span>
        <div class="contact-text">303.555.0142<br>888.555.0178</div>
      </li>
      <li class="contact-row">
        <span class="contact-icon"><svg viewBox="0 0 24 24" fill="none"><g fill="none" stroke="#fff" stroke-width="2"><circle cx="12" cy="12" r="9"/><ellipse cx="12" cy="12" rx="4" ry="9"/><path d="M3 12h18M5 7h14M5 17h14"/></g></svg></span>
        <div class="contact-text">daniel@keystonefloor.com<br>www.keystonefloor.com</div>
      </li>
      <li class="contact-row">
        <span class="contact-icon"><svg viewBox="0 0 24 24"><path d="M12 2a7 7 0 0 0-7 7c0 5 7 13 7 13s7-8 7-13a7 7 0 0 0-7-7zm0 9.5A2.5 2.5 0 1 1 12 6.5a2.5 2.5 0 0 1 0 5z"/></svg></span>
        <div class="contact-text">P.O. Box 2470<br>Lakeview, CO 80999</div>
      </li>
    </ul>
  </section>

  <section class="card card-back" aria-label="Business card back">
    <div class="accent-top"></div>
    <div class="brand">
      <div class="brand-mark"></div>
      <div class="brand-name">Keystone<br>Floor Review</div>
      <div class="tagline">Analysis &amp; Consulting</div>
    </div>
    <p class="service-line">Certified floor covering<br>inspections &amp; consulting</p>
    <div class="accent-bottom"></div>
  </section>
</body>
</html>
```